Appraisal and Umpire Services for Property Damage Insurance Claims

I need a banner design that I can post as an advertisement on industry web pages. I would like this to be elegant and reflective of quality, integrity and professionalism.

Target Market(s)

Insurance Companies and Attorneys

Industry/Entity Type

Insurance

Contact Information for Business Card

Gerald M. Hollis
918 Birchwell Lane
PO Box 582
Clifton Park, NY 12093
ghollis@brindlevault.com
Phone: (800) 555-0147, Ext. 2861
Direct: (315) 555-0189

Logo Text

Line One: Velmar Brook Claim Service, Inc. Line two: Appraisal and Umpire Services

Font styles to use
Serif
Sans Serif

Colors
0255a3
f78f20
faa54b
3176b5

Requirements
Must have
• New Logo and matching banner, business card and stationary.
• The colors must be orange and navy blue in the logo. I have selected them below.

```html
<!DOCTYPE html>
<html lang="en">
<head>
<meta charset="utf-8">
<title>Velmar Brook Claim Service – Appraisal &amp; Umpire Services</title>
<link rel="stylesheet" href="https://fonts.googleapis.com/css2?family=Montserrat:wght@400;500;700&family=Raleway:wght@400;500&display=swap">
<style>
  :root {
    --navy: #0255a3;
    --navy-deep: #1f2a5c;
    --blue: #3176b5;
    --orange: #f78f20;
    --orange-light: #faa54b;
    --ink: #1f2a5c;
    --rule: #c9ccd6;
    --white: #ffffff;
  }
  * { margin: 0; padding: 0; box-sizing: border-box; }
  html, body { width: 1200px; height: 2400px; overflow: hidden; background: var(--white); }
  .banner {
    position: relative;
    width: 1200px;
    height: 2400px;
    overflow: hidden;
    background: var(--white);
    font-family: "Montserrat", sans-serif;
  }
  .hero-photo {
    position: absolute;
    left: 0; top: 0;
    width: 1200px; height: 1400px;
    background:
      linear-gradient(180deg, rgba(255,255,255,1) 0%, rgba(255,255,255,0.95) 14%, rgba(255,255,255,0.2) 32%, rgba(255,255,255,0) 45%),
      linear-gradient(160deg, #8f9a8a 0%, #b8a58c 35%, #9c8672 60%, #7e7568 100%);
  }
  .hero-curve { position: absolute; left: 0; top: 1200px; width: 1200px; height: 220px; }
  .brand {
    position: absolute;
    top: 110px; left: 0; width: 1200px;
    text-align: center;
    color: var(--navy-deep);
    font-weight: 700;
  }
  .brand-name { font-size: 96px; line-height: 1; letter-spacing: 2px; }
  .brand-sub { font-size: 54px; line-height: 1; margin-top: 22px; letter-spacing: 4px; }
  .service-bar {
    position: absolute;
    left: 76px; top: 1510px;
    width: 9px; height: 320px;
    background: linear-gradient(180deg, var(--navy-deep) 0 55%, var(--orange-light) 55% 100%);
  }
  .service-title {
    position: absolute;
    left: 118px; top: 1490px;
    font-family: "Raleway", sans-serif;
    font-weight: 400;
    font-size: 98px;
    line-height: 112px;
    color: var(--ink);
  }
  .service-divider {
    position: absolute;
    left: 636px; top: 1510px;
    width: 3px; height: 320px;
    background: var(--rule);
  }
  .service-list {
    position: absolute;
    left: 676px; top: 1512px;
    list-style: none;
    font-family: "Raleway", sans-serif;
    font-weight: 500;
    font-size: 48px;
    line-height: 58px;
    color: var(--ink);
    letter-spacing: 1px;
  }
  .service-list li { margin-bottom: 32px; }
  .service-list li.two-line { margin-bottom: 0; }
  .cta {
    position: absolute;
    left: 316px; top: 1900px;
    width: 572px; height: 120px;
    border-radius: 14px;
    background: linear-gradient(180deg, #ffc21c 0%, var(--orange) 100%);
    color: var(--white);
    font-weight: 500;
    font-size: 64px;
    line-height: 120px;
    text-align: center;
    text-decoration: none;
  }
  .phone-band {
    position: absolute;
    left: 0; top: 2112px;
    width: 1200px; height: 288px;
    background: var(--navy-deep);
    color: var(--white);
    font-weight: 700;
    font-size: 104px;
    line-height: 288px;
    text-align: center;
    letter-spacing: 1px;
  }
</style>
</head>
<body>
<main class="banner">
  <div class="hero-photo" role="img" aria-label="Aerial photograph of a neighbourhood of mobile homes destroyed by a storm, with debris scattered across the ground"></div>
  <svg class="hero-curve" viewBox="0 0 1200 220" aria-hidden="true">
    <path d="M0 190 Q 640 170 1200 40 L1200 220 L0 220 Z" fill="#ffffff"/>
    <path d="M560 176 Q 900 140 1200 40" fill="none" stroke="#f78f20" stroke-width="10"/>
  </svg>

  <header class="brand">
    <div class="brand-name">VELMAR BROOK</div>
    <div class="brand-sub">CLAIM SERVICE, INC</div>
  </header>

  <div class="service-bar"></div>
  <h1 class="service-title">Appraisal<br>&amp; Umpire<br>Services</h1>
  <div class="service-divider"></div>
  <ul class="service-list">
    <li>PROPERTY</li>
    <li>CASUALTY</li>
    <li class="two-line">CLAIM<br>ADMINISTRATION</li>
  </ul>

  <a class="cta" href="#">Learn More</a>

  <footer class="phone-band">1-800-555-0147</footer>
</main>
</body>
</html>
```